Brightmoor Glowing - Two Pages of Information and Pictures

We need a two page summary of the Service Offerings of Brightmoor Glowing - a company that installs LED Lighting. We've written the copy and picked images and chart that we like and have laid it out a word document.

We're looking for someone to design a more professional page layout than the generic Word Template. Please do not feel the current layout is suggested. It is only laid out this way because Word had that template. Be as creative as you want.

We would like the images and text to be in the same order that it is in now.

We're also in a rush so speed is appreciated. THANK YOU !!

Target Market(s)

Corporate Offices in New York

Industry/Entity Type

Lighting Fixture

Colors
85cae6
87cfc7
9bcb3c
3377b5

Requirements
Must have
• Must include two pages of the copy and images written and provided in the word document that was uploaded. Must use the Brightmoor colors in the logo.
Nice to have
• An easy to read flow of images and.

```html
<!DOCTYPE html>
<html lang="en">
<head>
<meta charset="utf-8">
<title>Brightmoor Glowing – Service Overview</title>
<link href="https://fonts.googleapis.com/css2?family=Source+Sans+3:ital,wght@0,300;0,400;0,600;0,700;1,300;1,400&display=swap" rel="stylesheet">
<style>
  :root{
    --backdrop:#2e2e2e;
    --paper:#ffffff;
    --teal-light:#b9e0da;
    --teal-pale:#d7efeb;
    --slate:#6f9dab;
    --slate-dark:#5d8a98;
    --lime-pale:#d6e1a2;
    --lime:#8fc26a;
    --heading:#5b9cab;
    --body-grey:#9a9a9a;
    --body-dark:#3f3f3f;
    --ink:#222;
    --white:#ffffff;
  }
  *{box-sizing:border-box;margin:0;padding:0}
  html,body{width:1200px;height:1200px;overflow:hidden;background:var(--backdrop)}
  body{position:relative;font-family:"Source Sans 3",sans-serif}
  .page{position:absolute;top:225px;width:662px;height:939px;background:var(--paper);
    transform:scale(.8);transform-origin:0 0;overflow:hidden}
  .page--front{left:59px}
  .page--back{left:623px}
  .page svg.art{position:absolute;left:0;top:0}
  .front-heading{position:absolute;left:57px;top:440px;color:var(--heading);font-weight:700;font-size:22px;line-height:21px}
  .front-body{position:absolute;left:57px;top:512px;width:262px;color:var(--body-grey);font-weight:300;font-size:15.5px;line-height:19px}
  .quotes{position:absolute;left:299px;top:252px;width:296px;color:var(--white);text-align:center;font-size:15.5px;line-height:20.7px}
  .quotes-edge{float:left;width:54px;height:540px;
    shape-outside:polygon(0 0,16px 0,54px 100%,0 100%)}
  .quote{font-style:italic;font-weight:300;margin-bottom:20px}
  .quote cite{display:block;font-style:normal;font-weight:600;font-size:16px}
  .contact{position:absolute;left:57px;top:843px;color:var(--white);font-size:21px;line-height:24.5px;font-weight:400}
  .contact li{list-style:none;display:flex;align-items:center;gap:8px}
  .contact svg{flex:none}
  .brand{position:absolute;left:490px;top:833px;width:160px;text-align:center;color:var(--slate-dark);font-weight:300;font-size:15px;letter-spacing:1px}
  .tagline{position:absolute;right:8px;top:906px;color:var(--ink);font-size:15.5px;font-weight:300}
  .back-heading{position:absolute;left:57px;top:54px;color:var(--heading);font-weight:700;font-size:20px}
  .back-sub{position:absolute;left:57px;top:91px;color:var(--body-dark);font-style:italic;font-size:15px}
  .back-body{position:absolute;left:57px;top:129px;width:268px;color:var(--body-dark);font-size:12.3px;line-height:15.8px}
  .back-body p{margin-bottom:15.5px}
  .chart{position:absolute;left:340px;top:270px}
</style>
</head>
<body>

<section class="page page--front" aria-label="Front page">
  <svg class="art" width="662" height="939" viewBox="0 0 662 939">
    <polygon points="0,0 605,0 60,410 0,225" fill="#8a8270" role="img" aria-label="Photo of an open-plan office lit by filament pendant lamps"/>
    <polygon points="0,225 60,410 0,340" fill="var(--slate)"/>
    <polygon points="0,340 60,410 56,420 0,400" fill="var(--lime-pale)"/>
    <polygon points="605,0 662,0 662,25 60,420 56,410" fill="var(--teal-light)"/>
    <polygon points="662,25 662,95 70,425 60,420" fill="var(--teal-pale)"/>
    <polygon points="606,110 662,90 662,690 606,760" fill="var(--lime-pale)"/>
    <polygon points="606,69 299,276 336,791 606,791" fill="var(--slate)"/>
    <g fill="none" stroke="#fff" stroke-width="4">
      <path d="M515,160 c0,-20 22,-32 45,-32 c24,0 44,12 44,32 c0,18 -18,30 -40,31 l-18,14 l2,-16 c-20,-4 -33,-14 -33,-29z"/>
      <path d="M598,170 c14,6 22,15 22,27 c0,10 -6,18 -15,23 l3,14 l-15,-11"/>
    </g>
    <polygon points="0,800 190,834 0,834" fill="var(--lime-pale)"/>
    <polygon points="0,834 420,834 485,939 0,939" fill="var(--teal-light)"/>
  </svg>

  <h2 class="front-heading">No Upfront Cost –<br>Turnkey LEDs</h2>
  <p class="front-body">Brightmoor Glowing provides LED lighting as a service – fully implemented and managed LEDs at no upfront cost. Brightmoor takes the risk, hassle and capital cost out of adopting LED’s energy saving technology. Brightmoor guarantees net-savings for customers on day one, and continues to guarantee savings and performance for the full term of the contract. And the savings add up! A project can be installed 2-4 weeks from kickoff, and projects continue to generate savings for up to 10 years.</p>

  <div class="quotes">
    <div class="quotes-edge"></div>
    <p class="quote">“Brightmoor made a huge improvement in the lighting for our headquarters. The installation process was as smooth as can be and the service since has been excellent.” –<cite>Harborline Health</cite></p>
    <p class="quote">“In a museum, quality lighting is paramount. Brightmoor has been a great partner in helping us transition to LEDs that look great, save us money, and make lighting management so much simpler.” –<cite>Children’s Gallery of Art, New York</cite></p>
    <p class="quote">“We are so happy to have had Brightmoor’s help building out our new office space – they put their lighting expertise to work delivering beautiful LEDs and fixtures. It was cost-effective, removed lighting from the build-out budget, and it’s been a joy to work with them since.”<cite>Fieldmark, Inc</cite></p>
  </div>

  <ul class="contact">
    <li><svg width="20" height="16" viewBox="0 0 20 16"><rect x="1" y="1" width="18" height="14" fill="none" stroke="#fff" stroke-width="1.6"/><path d="M1,1 L10,9 L19,1" fill="none" stroke="#fff" stroke-width="1.6"/></svg>customers@brightmoorglowing.com</li>
    <li><svg width="20" height="18" viewBox="0 0 20 18"><path d="M10,2 c5,0 9,3 9,6.5 s-4,6.5 -9,6.5 l-5,3 l1,-4 c-3,-1 -5,-3 -5,-5.5 C1,5 5,2 10,2z" fill="none" stroke="#fff" stroke-width="1.6"/></svg>347 555 0142</li>
    <li><svg width="20" height="18" viewBox="0 0 20 18"><circle cx="10" cy="9" r="8" fill="#fff"/></svg>brightmoorglowing.com</li>
  </ul>
  <div class="brand">BRIGHTMOOR</div>
  <div class="tagline">Making LEDs beautiful.</div>
</section>

<section class="page page--back" aria-label="Back page">
  <svg class="art" width="662" height="939" viewBox="0 0 662 939">
    <polygon points="200,0 300,0 600,250 590,262" fill="var(--teal-light)"/>
    <polygon points="300,0 662,0 662,55 600,250" fill="#6b6660" role="img" aria-label="Photo of a lobby and a red ceiling with round light fixtures"/>
    <polygon points="662,55 662,75 598,258 600,250" fill="var(--lime-pale)"/>
    <circle cx="437" cy="574" r="110" fill="#8b8a86" stroke="var(--lime)" stroke-opacity=".7" stroke-width="8" role="img" aria-label="Photo of a lounge under a red ceiling with round lights"/>
    <circle cx="567" cy="659" r="107" fill="#9a8e80" stroke="var(--slate)" stroke-width="8" role="img" aria-label="Photo of a boardroom with linear LED fixtures"/>
    <circle cx="427" cy="734" r="78" fill="#a07a4e" stroke="var(--lime-pale)" stroke-width="8" role="img" aria-label="Photo of a wood-panelled meeting room"/>
    <polygon points="0,800 190,834 0,834" fill="var(--lime-pale)"/>
    <polygon points="0,834 420,834 485,939 0,939" fill="var(--teal-light)"/>
  </svg>

  <h2 class="back-heading">Brightmoor Glowing</h2>
  <p class="back-sub">Why use Brightmoor?</p>
  <div class="back-body">
    <p>Brightmoor’s customers understand the value of LEDs but don’t want to deal with the risk, hassle and capital cost on their own. Brightmoor starts saving customers money the first month – typically a net-savings of about 4.7 cents a square-foot per month. Brightmoor will design aesthetic LED systems and install the best available technology.</p>
    <p>Brightmoor provides LEDs at the best cost with its as-a-service structure, which puts the cost of lighting into clients’ monthly operating budget for less than they save. By installing projects immediately, Brightmoor eliminates the cost of foregone savings that would accumulate from delayed implementation.</p>
    <p>It can be risky to adopt new technology, especially when salespeople try to sell more than is needed. Brightmoor has access to better equipment and at better cost than is widely available on the open market and passes that quality and savings on to its customers. Brightmoor guarantees performance for 5 years, which removes the risk of a failed project. The Best Team in LEDs</p>
    <p>Brightmoor is a team of lighting experts who get the evolution of lighting and efficiency. Simply put, we come in up every day with one goal: to provide an excellent service that saves money and uses less electricity. Part of the team focuses on the supply chain of the very best equipment that customers have come to appreciate. Part of the team focuses on the project management of each installation. And, part of the team focuses on resolving any questions customers might have in their transition. Together we make up the best team in LEDs and work tirelessly to make it easy to upgrade.</p>
  </div>

  <svg class="chart" width="315" height="190" viewBox="0 0 315 190" font-family="Source Sans 3, sans-serif">
    <text x="158" y="11" text-anchor="middle" font-size="10.5" fill="#333">Annual and Total Net-Savings of 250,000 ft2 Customer</text>
    <g stroke="#e6e6e6" stroke-width=".7">
      <line x1="30" y1="34" x2="275" y2="34"/><line x1="30" y1="56" x2="275" y2="56"/>
      <line x1="30" y1="78" x2="275" y2="78"/><line x1="30" y1="100" x2="275" y2="100"/>
      <line x1="30" y1="122" x2="275" y2="122"/><line x1="30" y1="144" x2="275" y2="144"/>
      <line x1="30" y1="166" x2="275" y2="166"/>
    </g>
    <g font-size="5" fill="#555" text-anchor="end">
      <text x="26" y="36">$300</text><text x="26" y="58">$250</text><text x="26" y="80">$200</text>
      <text x="26" y="102">$150</text><text x="26" y="124">$100</text><text x="26" y="146">$50</text><text x="26" y="168">$-</text>
    </g>
    <g font-size="5" fill="#555">
      <text x="282" y="36">$2.0</text><text x="282" y="63">$1.6</text><text x="282" y="90">$1.2</text>
      <text x="282" y="117">$0.8</text><text x="282" y="144">$0.4</text><text x="282" y="168">$0.0</text>
    </g>
    <text transform="translate(8,120) rotate(-90)" font-size="5" fill="#555">Thousands</text>
    <text transform="translate(305,80) rotate(90)" font-size="5" fill="#555">Millions</text>
    <g fill="var(--teal-light)">
      <rect x="43" y="122" width="5" height="44"/><rect x="66" y="122" width="5" height="44"/>
      <rect x="89" y="122" width="5" height="44"/><rect x="112" y="122" width="5" height="44"/>
      <rect x="135" y="122" width="5" height="44"/>
    </g>
    <g fill="var(--lime)">
      <rect x="49" y="104" width="6" height="62"/><rect x="72" y="104" width="6" height="62"/>
      <rect x="95" y="104" width="6" height="62"/><rect x="118" y="104" width="6" height="62"/>
      <rect x="141" y="104" width="6" height="62"/><rect x="165" y="59" width="6" height="107"/>
      <rect x="188" y="59" width="6" height="107"/><rect x="211" y="59" width="6" height="107"/>
      <rect x="234" y="59" width="6" height="107"/><rect x="257" y="59" width="6" height="107"/>
    </g>
    <polyline points="48,166 71,155 94,144 117,133 140,122 166,103 189,85 212,67 235,50 260,34" fill="none" stroke="#999" stroke-width="1"/>
    <line x1="30" y1="166" x2="275" y2="166" stroke="#bbb" stroke-width=".7"/>
    <g font-size="5" fill="#555" text-anchor="middle">
      <text x="48" y="175">1</text><text x="71" y="175">2</text><text x="94" y="175">3</text><text x="117" y="175">4</text><text x="141" y="175">5</text>
      <text x="167" y="175">6</text><text x="190" y="175">7</text><text x="213" y="175">8</text><text x="236" y="175">9</text><text x="260" y="175">10</text>
    </g>
    <g font-size="4.5" fill="#555">
      <rect x="52" y="183" width="9" height="2" fill="var(--teal-light)"/><text x="63" y="186">Annual Service Cost</text>
      <rect x="130" y="183" width="9" height="2" fill="var(--lime)"/><text x="141" y="186">Annual Net Savings</text>
      <line x1="200" y1="184" x2="209" y2="184" stroke="#999"/><text x="211" y="186">Total Net-Savings</text>
    </g>
  </svg>

  <ul class="contact">
    <li><svg width="20" height="16" viewBox="0 0 20 16"><rect x="1" y="1" width="18" height="14" fill="none" stroke="#fff" stroke-width="1.6"/><path d="M1,1 L10,9 L19,1" fill="none" stroke="#fff" stroke-width="1.6"/></svg>customers@brightmoorglowing.com</li>
    <li><svg width="20" height="18" viewBox="0 0 20 18"><path d="M10,2 c5,0 9,3 9,6.5 s-4,6.5 -9,6.5 l-5,3 l1,-4 c-3,-1 -5,-3 -5,-5.5 C1,5 5,2 10,2z" fill="none" stroke="#fff" stroke-width="1.6"/></svg>347 555 0142</li>
    <li><svg width="20" height="18" viewBox="0 0 20 18"><circle cx="10" cy="9" r="8" fill="#fff"/></svg>brightmoorglowing.com</li>
  </ul>
  <div class="brand">BRIGHTMOOR</div>
  <div class="tagline">Making LEDs beautiful.</div>
</section>

</body>
</html>
```